Mentorvale needs a WordPress - Design

I am a personal, team and business coach and help my clients to develop their potential. I mainly work with individuals and teams, but this can also be in the context of a company.
My business is called "Mentorvale"

The main goal of this website is to promote my business and to attire new customers.
I also want to present my concepts and ideas about coaching and how I actually do coaching and consulting. This is also to inform potential customers what coaching actually is and what it's not.
I want to host this website on a hosting-provider and want to be able to add and adapt content on my own. I'm thus looking for a WordPress - design.

Content:

vision
• Why do I do this
• How do I do this
• What am I doing

Coaching
• Career development
• Conflicts
• What is coaching, why coaching
• Conduct of a session and of the whole consultation
Limits of coaching
• Examples of positive effects of coaching

Support concept

Blog about current topics

Left

About me

Contact form

Footer / disclaimer

The following topics are the most important parts of my daily work as a coach with my clients, maybe this helps to get choos a suitable design:
- personality development, analyzing aspects and patterns and showing their influence
- Improve collaboration and cooperation in teams
- Addressing and solving conflicts (private and business)
- Identify and foster motivation, drivers, goals and action patterns
- Define next steps for the further improvement
- Accompany reorientation in professional career
- Discovering and using the strengths of the customers

The major part of my work is direct conversation with the customer, on site or virtually. My job is to support the customer in recognizing his own ideas, goals and possibilities and to define next steps in the desired direction

Target Market(s)

Small businesses and private persons in serch of a professional coach

Industry/Entity Type

Consultant

Number of Pages Required

1 page

Font styles to use
Sans Serif

Requirements
Must have
• - Logo / Name (see attachment)
- Menu, fixed navigation
- content
- blog
- Footer (contact, disclaimer)

- I need a WordPress design suitable for Mobile and Desktop devices.
- I'm looking for a modern, friendly and easy to use web site.
- First page as Long-pager (scrolling), other pages as long-pager or standard
- Decent, friendly colors but still clear, simple
Nice to have
• - Panorama image (image changing on every load of the site)
- Quote (changing on every load of the site)

```html
<!DOCTYPE html>
<html lang="en">
<head>
<meta charset="utf-8">
<title>Mentorvale – Personal, Team and Business Coaching</title>
<link href="https://fonts.googleapis.com/css2?family=Poppins:wght@600;700&family=Roboto:wght@300;400;500;700&display=swap" rel="stylesheet">
<style>
:root{
  --brand:#2e2f8e;
  --brand-dark:#24257a;
  --ink:#333338;
  --muted:#6e6e76;
  --line:#e4e4e8;
  --slate:#6b6a78;
  --paper:#ffffff;
  --mist:#ececee;
  --field:#a8a8ac;
  --night:#2b2a2f;
}
*{margin:0;padding:0;box-sizing:border-box}
html,body{width:1200px;height:4041px;overflow:hidden}
body{position:relative;font-family:"Roboto",Arial,sans-serif;color:var(--ink);background:var(--paper)}
.abs{position:absolute}
section,header,footer{position:absolute;left:0;width:1200px}
a{color:inherit;text-decoration:none}

/* header */
.site-header{top:0;height:80px;background:#fff;border-bottom:1px solid var(--line)}
.brand{left:121px;top:24px;display:flex;align-items:center;gap:8px;font-size:16px;font-weight:500;color:var(--brand);letter-spacing:.5px}
.brand-mark{width:14px;height:14px;background:var(--brand)}
.main-nav{top:34px;font-size:14px;color:#7c7c84}
.main-nav a{position:absolute;transform:translateX(-50%);white-space:nowrap}
.main-nav .active{color:var(--brand)}
.main-nav .active::after{content:"";position:absolute;left:0;right:0;top:27px;height:2px;background:var(--brand)}
.nav-sep{position:absolute;left:1028px;top:-2px;width:2px;height:18px;background:#333}

/* hero */
.hero{top:80px;height:563px;overflow:hidden}
.hero-photo{position:absolute;inset:0;background:linear-gradient(120deg,#6e6a62 0%,#4a4a52 35%,#3c3d47 55%,#5e5a55 80%,#7b7268 100%)}
.hero-shade{position:absolute;inset:0;background:rgba(20,20,30,.35)}
.hero-title{top:225px;width:100%;text-align:center;font-family:"Poppins",Arial,sans-serif;font-weight:700;font-size:68px;color:#fff;letter-spacing:1px;line-height:80px}
.hero-lede{top:308px;left:300px;width:600px;text-align:center;color:#fff;font-size:15px;line-height:24px}
.btn{display:flex;align-items:center;justify-content:center;background:var(--brand);color:#fff;font-weight:500;border-radius:20px;font-size:14px}
.hero-btn{top:372px;left:515px;width:171px;height:34px}

/* about */
.about{top:643px;height:578px}
.about-dots{left:183px;top:57px;width:298px;height:380px;background:#f3f3f6}
.about-photo{left:212px;top:110px;width:364px;height:381px;background:linear-gradient(150deg,#6b7a8c,#4b5366 50%,#8a7a6c)}
.kicker{font-weight:700;color:var(--brand);font-size:20px}
.about-kicker{left:662px;top:88px}
.about-title{left:662px;top:130px;width:440px;font-size:26px;font-weight:500;line-height:31px;color:#3a3a40}
.about-text{left:662px;top:208px;width:400px;font-size:14px;line-height:25.7px;color:var(--muted)}
.about-btn{left:662px;top:438px;width:173px;height:36px}

/* coaching */
.coaching{top:1221px;height:922px;overflow:hidden}
.coaching-bg{position:absolute;inset:0;background:linear-gradient(135deg,#73727f,#65646f 50%,#6e6d79)}
.section-title{width:100%;text-align:center;font-weight:700;font-size:22px}
.coaching .section-title{top:82px;color:#fff}
.coaching-lede{top:124px;left:250px;width:700px;text-align:center;font-size:16px;line-height:23px;color:#f0f0f4;font-weight:300}
.service{width:260px;color:#fff}
.service svg{display:block;width:34px;height:34px}
.service h3{font-size:20px;font-weight:500;line-height:26px;margin-top:12px}
.service p{font-size:13px;line-height:21.5px;margin-top:22px;font-weight:400}
.service-card{left:433px;top:521px;width:333px;height:304px;background:#fff;border-radius:6px}
.service.featured{color:var(--brand)}
.service.featured p{color:#8a8a92}
.read-more{display:block;font-size:11px;color:#8a8a92;margin-top:14px}

/* vision */
.vision{top:2143px;height:294px}
.vision-band{left:0;top:0;width:480px;height:294px;background:linear-gradient(100deg,var(--brand) 0%,var(--brand) 68%,#fff 68.2%)}
.vision-person{left:290px;top:-41px;width:192px;height:335px;background:linear-gradient(180deg,#c9d6e3,#9fb3c8 60%,#d2c5b0);border-radius:90px 90px 0 0}
.vision-kicker{left:618px;top:68px}
.vision-list{left:634px;top:112px;list-style:none}
.vision-list li{display:flex;align-items:center;gap:14px;font-size:20px;color:#6e6e76;font-weight:300;height:50px}
.vision-list li:nth-child(3){margin-top:5px}

/* blog */
.blog{top:2437px;height:717px}
.blog .section-title{top:80px;color:var(--brand)}
.blog-lede{top:114px;left:275px;width:650px;text-align:center;font-size:16px;line-height:24px;color:var(--muted)}
.post{top:212px;width:305px;height:365px;background:#fff;box-shadow:0 2px 8px rgba(0,0,0,.08)}
.post-photo{height:168px}
.post-meta{position:absolute;left:16px;top:186px;display:flex;gap:18px;font-size:11px;color:#777}
.post-meta span{display:flex;align-items:center;gap:7px}
.post h3{position:absolute;left:15px;top:216px;font-size:15px;font-weight:500;color:#3a3a40}
.post p{position:absolute;left:16px;top:248px;width:270px;font-size:13px;line-height:19px;color:#8a8a92}
.post .post-link{position:absolute;left:16px;top:337px;font-size:12px;color:var(--brand)}
.pager{top:623px;left:548px;display:flex;gap:13px}
.pager i{width:10px;height:10px;border-radius:50%;border:1.5px solid var(--brand)}
.pager i.on{background:var(--brand)}

/* contact */
.contact{top:3154px;height:585px;background:var(--mist)}
.contact .section-title{top:80px;color:#3a3a40}
.field{background:var(--field);border:1px solid #8d8d92;color:#e6e6ea;font-size:13px;padding:10px}
.contact-btn{left:209px;top:464px;width:172px;height:38px}
.contact-title{left:595px;top:150px;font-size:29px;font-weight:500;line-height:36px;color:#333}
.contact-text{left:595px;top:236px;width:360px;font-size:13px;line-height:19px;color:#555}
.info{left:596px;display:flex;gap:24px}
.info-icon{width:42px;height:42px;background:#fff;display:flex;align-items:center;justify-content:center}
.info h4{font-size:17px;font-weight:500;color:#333;margin-top:4px}
.info p{font-size:12px;color:#555;margin-top:3px}

/* footer */
.site-footer{top:3739px;height:302px;background:var(--night);color:#fff}
.footer-nav{top:68px;width:100%;display:flex;justify-content:center;gap:33px;font-size:14px}
.social{top:112px;left:0;width:100%}
.social i{position:absolute;width:42px;height:42px;border-radius:50%;background:#fff}
.legal{top:193px;width:100%;display:flex;justify-content:center;gap:14px;font-size:12px;align-items:center}
.legal em{font-style:normal;color:#aaa;font-size:18px}
.copyright{top:262px;width:100%;text-align:center;font-size:10px;color:#ddd}
</style>
</head>
<body>

<header class="site-header">
  <a class="abs brand" href="#"><span class="brand-mark"></span>Mentorvale</a>
  <nav class="abs main-nav" style="left:0;width:1200px">
    <a class="active" style="left:551px">Home</a>
    <a style="left:626px">Vision</a>
    <a style="left:709px">Coaching</a>
    <a style="left:789px">Blog</a>
    <a style="left:866px">About Me</a>
    <a style="left:970px">Contact Us</a>
    <span class="nav-sep"></span>
    <svg style="position:absolute;left:1058px;top:-1px" width="18" height="18" viewBox="0 0 18 18" fill="none" stroke="#333" stroke-width="2"><circle cx="7.5" cy="7.5" r="5.5"/><path d="M11.5 11.5l5 5"/></svg>
  </nav>
</header>

<section class="hero">
  <div class="hero-photo" role="img" aria-label="Photo of a coaching team meeting around a table"></div>
  <div class="hero-shade"></div>
  <h1 class="abs hero-title">MENTORVALE</h1>
  <p class="abs hero-lede">Quis ipsum suspendisse ultrices gravidaisus commodo viverra maecenas accumsan lacus vel facilisis</p>
  <a class="abs btn hero-btn" href="#">GET STARTED</a>
</section>

<section class="about">
  <div class="abs about-dots" role="img" aria-label="Decorative dotted backdrop"></div>
  <div class="abs about-photo" role="img" aria-label="Photo of a coach presenting ideas to a team at a whiteboard"></div>
  <h2 class="abs kicker about-kicker">ABOUT ME</h2>
  <h3 class="abs about-title">Consectetur Adipiscing Elitsedo Riusmod Iempor</h3>
  <p class="abs about-text">Ratus error sit voluptatem accusantium doloremque laudantium, totam rem aperiam, eaque ipsa quae ab illo inventore veritatis et quasi architecto beatae vitae dicta sunt explicabo. Nemo enim ipsam voluptatem quia voluptas sit aspernatur aut odit aut fugit, sed quia consequuntur magni dolores eos qui ratione voluptatem sequi nesciunt. Neque porro quisquam est, qui dolorem ipsum quia dolor sit amet, consectetur</p>
  <a class="abs btn about-btn" href="#">READ MORE</a>
</section>

<section class="coaching">
  <div class="coaching-bg" role="img" aria-label="Muted photo of a workshop behind the coaching topics"></div>
  <h2 class="abs section-title">COACHING</h2>
  <p class="abs coaching-lede">Ratus error sit voluptatem accusantium doloremque laudantium totam rem aperiam eaque ipsa quae ab illo inventore veritatis et quasi architecto</p>

  <div class="abs service" style="left:115px;top:251px">
    <svg viewBox="0 0 34 34" fill="none" stroke="#fff" stroke-width="1.6"><path d="M3 14l14-10 14 10v16H3z"/><path d="M3 14l14 10 14-10"/><path d="M9 10h16v9"/></svg>
    <h3>Career Development</h3>
    <p>Eatus error sit voluptatem accusantium doloremque laudantium, totam rem aperiam, eaque ipsa quae ab illo inventore veritatis et quasi architecto beatae vitae dicta sunt explicabo.</p>
  </div>
  <div class="abs service" style="left:475px;top:251px">
    <svg viewBox="0 0 34 34" fill="none" stroke="#fff" stroke-width="1.6"><rect x="3" y="3" width="28" height="28"/><path d="M12 3v28M22 3v28M6 9h3M15 9h4M25 9h3"/></svg>
    <h3>Conflicts</h3>
    <p>Eatus error sit voluptatem accusantium doloremque laudantium, totam rem aperiam, eaque ipsa quae ab illo inventore veritatis et quasi architecto beatae vitae dicta sunt explicabo.</p>
  </div>
  <div class="abs service" style="left:836px;top:251px">
    <svg viewBox="0 0 34 34" fill="none" stroke="#fff" stroke-width="1.6"><rect x="8" y="3" width="20" height="13"/><circle cx="7" cy="21" r="3"/><circle cx="17" cy="21" r="3"/><circle cx="27" cy="21" r="3"/><path d="M2 31c0-4 10-4 10 0M12 31c0-4 10-4 10 0M22 31c0-4 10-4 10 0"/></svg>
    <h3>What is coaching,<br>why coaching</h3>
    <p>Eatus error sit voluptatem accusantium doloremque laudantium, totam rem aperiam, eaque ipsa quae ab illo inventore veritatis et quasi architecto beatae vitae dicta sunt explicabo.</p>
  </div>

  <div class="abs service" style="left:115px;top:568px">
    <svg viewBox="0 0 34 34" fill="none" stroke="#fff" stroke-width="1.6"><circle cx="17" cy="7" r="4"/><path d="M10 19c0-6 14-6 14 0"/><rect x="4" y="22" width="26" height="6"/><circle cx="6" cy="16" r="2.5"/><circle cx="28" cy="16" r="2.5"/></svg>
    <h3>Conduct of a session and<br>of the whole consultation</h3>
    <p>Eatus error sit voluptatem accusantium doloremque laudantium, totam rem aperiam, eaque ipsa quae ab illo inventore veritatis et quasi architecto beatae vitae dicta sunt explicabo.</p>
  </div>
  <div class="abs service-card"></div>
  <div class="abs service featured" style="left:475px;top:568px">
    <svg viewBox="0 0 34 34" fill="none" stroke="#2e2f8e" stroke-width="1.6"><rect x="9" y="3" width="16" height="10"/><circle cx="8" cy="19" r="3"/><circle cx="17" cy="19" r="3"/><circle cx="26" cy="19" r="3"/><path d="M3 31c0-5 10-5 10 0M12 31c0-5 10-5 10 0M21 31c0-5 10-5 10 0"/></svg>
    <h3>Limits of coaching</h3>
    <p>Eatus error sit voluptatem accusantium doloremque laudantium, totam rem aperiam, eaque ipsa quae ab illo inventore veritatis et quasi architecto beatae vitae dicta sunt explicabo.</p>
    <a class="read-more" href="#">Read More...</a>
  </div>
  <div class="abs service" style="left:836px;top:568px">
    <svg viewBox="0 0 34 34" fill="none" stroke="#fff" stroke-width="1.6"><rect x="6" y="3" width="25" height="17"/><path d="M11 15l5-5 4 3 6-6"/><circle cx="6" cy="23" r="3"/><path d="M1 32c0-5 10-5 10 0"/></svg>
    <h3>Examples of positive<br>effects of coaching</h3>
    <p>Eatus error sit voluptatem accusantium doloremque laudantium, totam rem aperiam, eaque ipsa quae ab illo inventore veritatis et quasi architecto beatae vitae dicta sunt explicabo.</p>
  </div>
</section>

<section class="vision">
  <div class="abs vision-band"></div>
  <div class="abs vision-person" role="img" aria-label="Portrait photo of the coach in a light blue shirt"></div>
  <h2 class="abs kicker vision-kicker">VISION</h2>
  <ul class="abs vision-list">
    <li><svg width="24" height="16" viewBox="0 0 24 16"><path d="M6 15a5 5 0 0 1-1-10 7 7 0 0 1 13 1 4.5 4.5 0 0 1 0 9z" fill="#2e2f8e"/><path d="M8 9l3 3 5-5" stroke="#fff" stroke-width="2" fill="none"/></svg>How do I do this</li>
    <li><svg width="24" height="16" viewBox="0 0 24 16"><path d="M6 15a5 5 0 0 1-1-10 7 7 0 0 1 13 1 4.5 4.5 0 0 1 0 9z" fill="#2e2f8e"/><path d="M8 9l3 3 5-5" stroke="#fff" stroke-width="2" fill="none"/></svg>Why do I do this</li>
    <li><svg width="24" height="16" viewBox="0 0 24 16"><path d="M6 15a5 5 0 0 1-1-10 7 7 0 0 1 13 1 4.5 4.5 0 0 1 0 9z" fill="#2e2f8e"/><path d="M8 9l3 3 5-5" stroke="#fff" stroke-width="2" fill="none"/></svg>What am I doing</li>
  </ul>
</section>

<section class="blog">
  <h2 class="abs section-title">BLOG</h2>
  <p class="abs blog-lede">Nemo enim ipsam voluptatem quia voluptas sit aspernatur aut odit aut fugit, sed quia consequuntur magni dolores eosui ratione</p>

  <article class="abs post" style="left:111px">
    <div class="post-photo" role="img" aria-label="Photo of two businessmen talking in an office" style="background:linear-gradient(135deg,#8fa0b2,#56606e 60%,#a49a8e)"></div>
    <div class="post-meta"><span><svg width="11" height="11" viewBox="0 0 11 11" fill="#2e2f8e"><circle cx="5.5" cy="3" r="2.6"/><path d="M0 11c0-5 11-5 11 0z"/></svg>5th June, 2020</span><span><svg width="16" height="10" viewBox="0 0 16 10" fill="#2e2f8e"><ellipse cx="8" cy="5" rx="8" ry="5"/></svg>23</span></div>
    <h3>Consequuntur Eagni Yolores</h3>
    <p>Eatus error sit voluptatem accusantium doloremque laudantium, totam rem aperiam, eaque ipsa.</p>
    <a class="post-link" href="#">Read More....</a>
  </article>
  <article class="abs post" style="left:447px">
    <div class="post-photo" role="img" aria-label="Photo of colleagues reviewing work on a laptop" style="background:linear-gradient(135deg,#6f9bc4,#3f5e82 55%,#c7b8a3)"></div>
    <div class="post-meta"><span><svg width="11" height="11" viewBox="0 0 11 11" fill="#2e2f8e"><circle cx="5.5" cy="3" r="2.6"/><path d="M0 11c0-5 11-5 11 0z"/></svg>5th June, 2020</span><span><svg width="16" height="10" viewBox="0 0 16 10" fill="#2e2f8e"><ellipse cx="8" cy="5" rx="8" ry="5"/></svg>23</span></div>
    <h3>Ratione Eoluptatem Tequi Wesciunt</h3>
    <p>Eatus error sit voluptatem accusantium doloremque laudantium, totam rem aperiam, eaque ipsa.</p>
    <a class="post-link" href="#">Read More....</a>
  </article>
  <article class="abs post" style="left:783px">
    <div class="post-photo" role="img" aria-label="Photo of a team meeting around a desk" style="background:linear-gradient(135deg,#a89a8a,#5a5456 55%,#c9b49c)"></div>
    <div class="post-meta"><span><svg width="11" height="11" viewBox="0 0 11 11" fill="#2e2f8e"><circle cx="5.5" cy="3" r="2.6"/><path d="M0 11c0-5 11-5 11 0z"/></svg>5th June, 2020</span><span><svg width="16" height="10" viewBox="0 0 16 10" fill="#2e2f8e"><ellipse cx="8" cy="5" rx="8" ry="5"/></svg>23</span></div>
    <p>Eatus error sit voluptatem accusantium doloremque laudantium, totam rem aperiam, eaque ipsa.</p>
    <a class="post-link" href="#">Read More....</a>
  </article>

  <div class="abs pager"><i class="on"></i><i></i><i></i><i></i><i></i></div>
</section>

<section class="contact">
  <h2 class="abs section-title">CONTACT US</h2>
  <div class="abs field" style="left:111px;top:158px;width:170px;height:38px">Name *</div>
  <div class="abs field" style="left:309px;top:158px;width:170px;height:38px">Email *</div>
  <div class="abs field" style="left:111px;top:221px;width:170px;height:38px">Phone *</div>
  <div class="abs field" style="left:309px;top:221px;width:170px;height:38px">Coaching *</div>
  <div class="abs field" style="left:111px;top:291px;width:368px;height:151px">Message *</div>
  <a class="abs btn contact-btn" href="#">SUBMIT</a>

  <h3 class="abs contact-title">Get In Touch For Any Kind<br>Of Help &amp; Informations</h3>
  <p class="abs contact-text">Eoluptatem accusantium doloremque laudantium, totam rem aperiam, eaque ipsa quae ab illo inventore veritatis et quasi architecto beatae</p>

  <div class="abs info" style="top:310px">
    <div class="info-icon"><svg width="16" height="20" viewBox="0 0 16 20"><path d="M8 0a8 8 0 0 1 8 8c0 6-8 12-8 12S0 14 0 8a8 8 0 0 1 8-8z" fill="#2e2f8e"/><circle cx="8" cy="8" r="3" fill="#fff"/></svg></div>
    <div><h4>Office Address:</h4><p>418 Linden Park Road, ASHBROOK, USA</p></div>
  </div>
  <div class="abs info" style="top:387px">
    <div class="info-icon"><svg width="16" height="16" viewBox="0 0 16 16"><path d="M3 1l3 3-2 2a9 9 0 0 0 6 6l2-2 3 3-2 2C7 15 1 9 1 3z" fill="#2e2f8e"/></svg></div>
    <div><h4>Call For Help:</h4><p>555 014 2280, 555 014 7391</p></div>
  </div>
  <div class="abs info" style="top:464px">
    <div class="info-icon"><svg width="20" height="14" viewBox="0 0 20 14" fill="none" stroke="#2e2f8e" stroke-width="1.6"><rect x="1" y="1" width="18" height="12"/><path d="M1 1l9 7 9-7"/></svg></div>
    <div><h4>Mail Us for Information</h4><p>hello@mentorvale.example</p></div>
  </div>
</section>

<footer class="site-footer">
  <nav class="abs footer-nav"><a>Home</a><a>Vision</a><a>Coaching</a><a>Blog</a><a>About Me</a><a>Contact Us</a></nav>
  <div class="abs social" aria-label="Social links">
    <i style="left:462px"></i><i style="left:539px"></i><i style="left:618px"></i><i style="left:694px"></i>
  </div>
  <nav class="abs legal"><a>Privacy Policy</a><em>/</em><a>Investor</a><em>/</em><a>Coaching</a><em>/</em><a>Legals</a></nav>
  <p class="abs copyright">Copyrights © 2020 All Rights Reserved</p>
</footer>

</body>
</html>
```